Interior Designer Branding Package

I need a full branding Package for print.
Business Card, Folder, Letter Head (Stationary) Note Pad, & Individual postcard type describing services, etc..
I also need a logo to add to a tote bag that will be part of my first initial client meeting.
I am an interior designer & furniture designer.
www.lumvarostudio.com
I have included some samples of what I am looking for & a sample of the tote bags I am thinking of embroidering the logo etc.. on the burlap portion.
Target Market(s)
High End -Full Interior Design Services: For Residential Customers
Industry/Entity Type
Business
Contact Information for Business Card
Company Name
Logo
Services-website-email-phone
Requirements
Nice to have
- Look sophisticated, bold, creative design

```html
<!DOCTYPE html>
<html lang="en">
<head>
<meta charset="utf-8">
<title>Lumvaro Studio — Stationery Set</title>
<link href="https://fonts.googleapis.com/css2?family=Questrial&display=swap" rel="stylesheet">
<style>
  :root{
    --backdrop:#d8d8d8;
    --paper:#ffffff;
    --ink:#2a2a2a;
    --ink-soft:#555555;
    --charcoal:#2b2b2b;
    --charcoal-edge:#3a3a3a;
    --on-dark:#f2f2f2;
    --signature-tone:#b9c3e8;
  }
  *{margin:0;padding:0;box-sizing:border-box}
  html,body{width:1200px;height:1000px;overflow:hidden}
  body{background:var(--backdrop);font-family:"Questrial",sans-serif;color:var(--ink);position:relative}
  .piece{position:absolute}
  .paper{background:var(--paper);border:1px solid #cfcfcf}
  .dark{background:var(--charcoal);color:var(--on-dark)}

  .brand{display:flex;align-items:center;gap:6px;letter-spacing:.06em;text-transform:uppercase;line-height:1}
  .brand-square{display:inline-block;border:1px solid currentColor}

  /* Letterhead */
  .letterhead{left:226px;top:100px;width:424px;height:534px}
  .letterhead .brand{position:absolute;right:97px;top:150px;font-size:11px}
  .letterhead .brand-square{width:14px;height:14px}
  .letter-contact{position:absolute;right:97px;top:186px;text-align:right;font-size:4.6px;line-height:6.2px;color:var(--ink-soft)}
  .letter-contact b{color:var(--ink)}
  .letter-body{position:absolute;left:36px;top:170px;width:290px;font-size:5.2px;line-height:6.6px;color:var(--ink-soft)}
  .letter-body .date{margin-bottom:9px}
  .letter-body .address{margin-bottom:25px}
  .letter-body .salutation{color:var(--ink);font-weight:bold;margin-bottom:6px}
  .letter-body p{margin-bottom:6.6px}
  .sign-off{margin-top:12px;display:flex;align-items:flex-start;gap:14px}
  .sign-off b{color:var(--ink)}
  .signature{width:80px;height:34px;background:linear-gradient(90deg,transparent,var(--signature-tone) 40%,transparent);opacity:.5;border-radius:2px;margin-top:-6px}

  /* Folder */
  .folder{left:636px;top:102px;width:370px;height:534px;border-radius:3px;background:linear-gradient(90deg,#262626,var(--charcoal) 40%,#303030)}
  .folder-spine{position:absolute;left:12px;top:0;bottom:0;border-left:1px solid var(--charcoal-edge)}
  .folder .brand{position:absolute;left:0;right:0;top:150px;flex-direction:column;gap:10px;font-size:19px}
  .folder .brand-square{width:34px;height:34px}
  .folder-url{position:absolute;left:0;right:0;bottom:20px;text-align:center;font-size:5.6px;letter-spacing:.04em}

  /* Business cards */
  .card-front{left:91px;top:671px;width:157px;height:87px}
  .card-front .brand{position:absolute;right:18px;top:10px;font-size:7.5px;gap:4px}
  .card-front .brand-square{width:9px;height:9px}
  .card-name{position:absolute;left:10px;top:43px;font-size:4.8px;letter-spacing:.04em;font-weight:bold;color:var(--ink)}
  .card-role{position:absolute;left:10px;top:50px;font-size:3.8px;color:var(--ink-soft)}
  .card-contact{position:absolute;left:10px;top:63px;font-size:3.6px;line-height:5.4px;color:var(--ink-soft)}
  .card-back{left:91px;top:784px;width:157px;height:86px}
  .card-back .brand{position:absolute;left:0;right:0;top:26px;flex-direction:column;gap:6px;font-size:8.5px}
  .card-back .brand-square{width:12px;height:12px}

  /* Envelope front */
  .envelope-front{left:281px;top:680px;width:381px;height:190px}
  .envelope-front .brand{position:absolute;left:18px;top:18px;font-size:9.5px}
  .envelope-front .brand-square{width:13px;height:13px}

  /* Envelope back */
  .envelope-back{left:707px;top:680px;width:382px;height:190px}
  .envelope-flap{position:absolute;left:0;top:0;width:382px;height:46px}
  .flap-mark{position:absolute;left:0;right:0;top:20px;text-align:center;font-size:5.5px;letter-spacing:.1em;color:var(--on-dark);text-transform:uppercase}
</style>
</head>
<body>

<section class="piece paper letterhead" aria-label="Letterhead">
  <div class="brand"><span class="brand-square"></span>Lumvaro Studio</div>
  <div class="letter-contact">
    <div><b>T:</b> 323.555.0142</div>
    <div><b>F:</b> 323.555.0187</div>
    <div><b>E:</b> clara@lumvarostudio.com</div>
    <div><b>W:</b> www.lumvarostudio.com</div>
  </div>
  <div class="letter-body">
    <div class="date">30.02.2015</div>
    <div class="address">Recipient's name<br>Lindenweg 14<br>10115 Berlin<br>Germany</div>
    <div class="salutation">Dear sir,</div>
    <p>Communication sits at the heart of every project we shape. A letter carries the care of a considered room, calm, clear and made to last. We believe each space begins with a conversation and grows through attention to detail.</p>
    <p>Thank you for the opportunity to present our services. Our studio offers full interior design for residential clients, from first sketch to final styling, along with custom furniture built for each home.</p>
    <p>Enclosed you will find an outline of our process, a schedule for the first meeting and a summary of fees. Please review them at your convenience and let us know any questions.</p>
    <p>We look forward to creating a space that feels entirely your own.</p>
    <div class="sign-off">
      <div>Yours Sincerely,<br><b>Elin Vasquez</b></div>
      <div class="signature" role="img" aria-label="Handwritten signature"></div>
    </div>
  </div>
</section>

<section class="piece folder dark" aria-label="Presentation folder">
  <div class="folder-spine"></div>
  <div class="brand"><span class="brand-square"></span>Lumvaro Studio</div>
  <div class="folder-url">www.lumvarostudio.com</div>
</section>

<section class="piece paper card-front" aria-label="Business card front">
  <div class="brand"><span class="brand-square"></span>Lumvaro Studio</div>
  <div class="card-name">CLARA BENETTI ROWE</div>
  <div class="card-role">Furniture &amp; Interior Designer</div>
  <div class="card-contact">T: 323.555.0142 · F: 323.555.0187 · E: clara@lumvarostudio.com<br>www.lumvarostudio.com</div>
</section>

<section class="piece dark card-back" aria-label="Business card back">
  <div class="brand"><span class="brand-square"></span>Lumvaro Studio</div>
</section>

<section class="piece paper envelope-front" aria-label="Envelope front">
  <div class="brand"><span class="brand-square"></span>Lumvaro Studio</div>
</section>

<section class="piece paper envelope-back" aria-label="Envelope back">
  <svg class="envelope-flap" viewBox="0 0 382 46" aria-hidden="true">
    <polygon points="0,0 382,0 382,10 352,46 30,46 0,10" fill="var(--charcoal)"/>
  </svg>
  <div class="flap-mark">Lumvaro</div>
</section>

</body>
</html>
```